WEMLIS Recruitment 2014

We need an e-mailable and US mailable print postcard postcard (same design) advertising the benefits of membership in the professional association, WEMLIS. I have a brochure design that Ive attached, so you can see what content we have included before. We are looking for something bright, catchy, and with less text than the 3-fold brochure we have used in the past. Also need new photos - stock photos are OK, but I may be able to send you some from our collection too.

```html
<!DOCTYPE html>
<html lang="en">
<head>
<meta charset="utf-8">
<title>WEMLIS Membership Postcard</title>
<link href="https://fonts.googleapis.com/css2?family=Merriweather:wght@700;900&family=PT+Sans:wght@400&display=swap" rel="stylesheet">
<style>
  :root {
    --navy: #27378f;
    --yellow: #fde01a;
    --white: #ffffff;
    --rule: #3341a0;
  }
  * { margin: 0; padding: 0; box-sizing: border-box; }
  html, body { width: 1200px; height: 857px; overflow: hidden; background: var(--white); }
  .postcard { position: relative; width: 1200px; height: 857px; background: var(--white); }
  .info-panel {
    position: absolute; left: 0; top: 0; width: 610px; height: 705px;
    background: var(--navy); color: var(--white);
  }
  .benefit { position: absolute; left: 34px; width: 542px; }
  .benefit-title {
    font-family: "Merriweather", Georgia, serif; font-weight: 900;
    font-size: 16.5px; line-height: 23px; color: var(--yellow);
    text-transform: uppercase; letter-spacing: 0.2px;
  }
  .benefit-title::before { content: "\2022"; margin-right: 6px; }
  .benefit-text {
    font-family: "PT Sans", Arial, sans-serif; font-size: 17.3px; line-height: 23px;
    text-align: justify;
  }
  .contact-band {
    position: absolute; left: 0; top: 705px; width: 610px; height: 152px;
    background: var(--yellow); color: var(--navy); padding: 12px 0 0 33px;
    font-family: "PT Sans", Arial, sans-serif; font-size: 17.3px; line-height: 23px;
  }
  .contact-name {
    font-family: "Merriweather", Georgia, serif; font-weight: 900;
    font-size: 16.5px; text-transform: uppercase; letter-spacing: 0.3px;
  }
  .mail-side { position: absolute; left: 610px; top: 0; width: 590px; height: 857px; }
  .stamp-box {
    position: absolute; left: 385px; top: 52px; width: 153px; height: 191px;
    border: 1.3px solid var(--rule);
  }
  .address-line { position: absolute; height: 0; border-top: 1.3px solid var(--rule); }
</style>
</head>
<body>
<main class="postcard">
  <section class="info-panel">
    <div class="benefit" style="top:30px">
      <h2 class="benefit-title">Active Membership</h2>
      <p class="benefit-text">Any educator whose professional functions are in admissions, enrollment management, financial aid, institutional research, records, registration, technology, or closely related areas in a Member Institution.</p>
    </div>
    <div class="benefit" style="top:166px">
      <h2 class="benefit-title">Associate Membership</h2>
      <p class="benefit-text">Persons, organizations, corporations, agencies, or candidates for institutional accreditation, which are found to have parallel purposes to the Association.</p>
    </div>
    <div class="benefit" style="top:281px">
      <h2 class="benefit-title">Extended Membership &amp; Retired Members</h2>
      <p class="benefit-text">Active members who leave the profession due to retirement or employment in other fields may elect to continue their membership.</p>
    </div>
    <div class="benefit" style="top:372px">
      <h2 class="benefit-title">Honorary Membership</h2>
      <p class="benefit-text">Persons who, after long and valued membership in the Association, have transferred their activities to other education fields, but still evidence an interest in the welfare of the Association, or any person who though not actively engaged in the profession.</p>
    </div>
    <div class="benefit" style="top:510px">
      <h2 class="benefit-title">Membership Fees</h2>
      <p class="benefit-text">Annual dues are $125 for each Institutional Membership and for each Associate Member.</p>
    </div>
    <div class="benefit" style="top:600px">
      <h2 class="benefit-title">Non-Profit Tax Number</h2>
      <p class="benefit-text">WEMLIS's non-profit tax number for reporting purposes is YA-90-4407215.</p>
    </div>
  </section>

  <footer class="contact-band">
    <p class="contact-name">Corinne Hallway</p>
    <p>WEMLIS VP for Membership Westbrook College of California</p>
    <p>218 Larchmont Road Fairhaven, CA&nbsp; 94977</p>
    <p>(415) 555-0148</p>
    <p>Challway@westbrook.edu</p>
  </footer>

  <section class="mail-side" aria-label="Mailing side">
    <div class="stamp-box" aria-label="Stamp area"></div>
    <div class="address-line" style="left:66px; top:353px; width:472px"></div>
    <div class="address-line" style="left:66px; top:439px; width:472px"></div>
    <div class="address-line" style="left:66px; top:525px; width:472px"></div>
    <div class="address-line" style="left:259px; top:611px; width:279px"></div>
  </section>
</main>
</body>
</html>
```